Offers Leaflet / Poster

We are a schoolwear provider, looking to create a leaflet/poster advertising offers across the 10 weeks school holidays.

The idea is to make it look like a test paper, with 10/10 marks. Please see a version we created in 2019. I would like something along very similar lines, but with a slightly more professional look or possibly a new twist on the same idea.

Please also see a document attached outlining the offers we would like to run + dates.

Many thanks

```html
<!DOCTYPE html>
<html lang="en">
<head>
<meta charset="UTF-8">
<title>Pembridge Schoolwear – Summer Offers</title>
<link href="https://fonts.googleapis.com/css2?family=Kaushan+Script&family=Arimo:wght@400;700&display=swap" rel="stylesheet">
<style>
  :root{
    --page:#ffffff;
    --navy:#1d3b6b;
    --navy-deep:#142c55;
    --navy-light:#2f5a93;
    --paper:#f8f6e2;
    --rule:#b9d3ea;
    --margin:#e8a0a0;
    --ink:#1f3f86;
    --red:#d9262c;
    --white:#ffffff;
  }
  *{box-sizing:border-box;margin:0;padding:0}
  html,body{width:863px;height:1200px;overflow:hidden;background:var(--page)}
  .canvas{position:relative;width:863px;height:1200px}
  .poster{
    position:absolute;left:80px;top:79px;width:708px;height:986px;overflow:hidden;
    background:
      radial-gradient(ellipse at 20% 15%,rgba(70,110,170,.45),transparent 55%),
      radial-gradient(ellipse at 85% 70%,rgba(60,100,160,.35),transparent 50%),
      radial-gradient(ellipse at 30% 90%,rgba(10,30,70,.4),transparent 55%),
      linear-gradient(160deg,var(--navy-light),var(--navy) 45%,var(--navy-deep));
  }
  .brand{
    position:absolute;left:0;top:60px;width:100%;
    display:flex;align-items:center;justify-content:center;gap:18px;
  }
  .brand-dot{width:40px;height:40px;border-radius:50%;background:var(--white)}
  .brand-name{
    font-family:"Arimo",Arial,sans-serif;font-weight:400;font-size:40px;line-height:1;
    color:var(--white);letter-spacing:.5px;
  }
  .headline{
    position:absolute;left:0;top:150px;width:100%;text-align:center;
    font-family:"Kaushan Script",cursive;font-weight:400;font-size:38px;color:var(--white);letter-spacing:.5px;
  }
  .sheet{
    position:absolute;left:99px;top:225px;width:521px;height:602px;
    background:
      linear-gradient(90deg,transparent 31px,var(--margin) 31px,var(--margin) 32px,transparent 32px),
      repeating-linear-gradient(180deg,transparent 0 24.8px,var(--rule) 24.8px 25.8px),
      var(--paper);
    background-position:0 0,0 14px,0 0;
    box-shadow:6px 8px 14px rgba(0,0,0,.45);
  }
  .holes{
    position:absolute;left:3px;top:12px;width:10px;height:578px;
    background:radial-gradient(circle,#111 3.5px,transparent 4px) 0 0/10px 26.2px repeat-y;
  }
  .offers{list-style:none;position:absolute;left:0;top:42px;width:100%}
  .offer{position:relative;height:52px}
  .week{position:absolute;left:44px;top:-6px;width:56px;height:50px}
  .week svg{position:absolute;inset:0}
  .week-label{
    position:absolute;inset:8px 0 0 0;text-align:center;
    font-family:"Kaushan Script",cursive;font-size:12px;line-height:14px;color:var(--ink);
  }
  .discount{position:absolute;left:106px;top:3px;font-family:"Kaushan Script",cursive;font-size:21px;color:var(--red)}
  .item{position:absolute;left:192px;top:9px;font-family:"Kaushan Script",cursive;font-size:13px;color:var(--ink);letter-spacing:.3px;white-space:nowrap}
  .dates{position:absolute;left:368px;top:10px;font-family:"Arimo",Arial,sans-serif;font-weight:700;font-size:14px;color:var(--ink);white-space:nowrap}
  .tagline{position:absolute;left:63px;top:884px;font-family:"Arimo",Arial,sans-serif;font-weight:700;font-size:19px;color:var(--white)}
  .tagline-script{position:absolute;left:63px;top:910px;font-family:"Kaushan Script",cursive;font-size:30px;color:var(--white)}
  .score{position:absolute;left:546px;top:862px;width:126px;height:92px}
  .score svg{position:absolute;inset:0}
  .score-text{position:absolute;inset:0;display:flex;align-items:center;justify-content:center;font-family:"Kaushan Script",cursive;font-size:30px;color:var(--white);transform:rotate(-8deg)}
</style>
</head>
<body>
<div class="canvas">
  <section class="poster">
    <header class="brand">
      <span class="brand-name">Pembridge Schoolwear</span>
      <span class="brand-dot"></span>
    </header>
    <h1 class="headline">Test out Pembridge This Summer</h1>

    <div class="sheet">
      <div class="holes"></div>
      <ol class="offers">
        <li class="offer"><div class="week"><svg viewBox="0 0 56 50"><path d="M30 3C12 2 3 14 4 27c1 14 13 21 27 19 15-2 22-11 21-24C51 9 42 3 26 5" fill="none" stroke="#d9262c" stroke-width="2"/></svg><div class="week-label">WEEK<br>1</div></div><span class="discount">10% OFF</span><span class="item">SOCKS</span><span class="dates">01/07/24 – 07/07/24</span></li>
        <li class="offer"><div class="week"><svg viewBox="0 0 56 50"><path d="M30 3C12 2 3 14 4 27c1 14 13 21 27 19 15-2 22-11 21-24C51 9 42 3 26 5" fill="none" stroke="#d9262c" stroke-width="2"/></svg><div class="week-label">WEEK<br>2</div></div><span class="discount">10% OFF</span><span class="item">NAME TAPES</span><span class="dates">08/07/24 – 14/07/24</span></li>
        <li class="offer"><div class="week"><svg viewBox="0 0 56 50"><path d="M30 3C12 2 3 14 4 27c1 14 13 21 27 19 15-2 22-11 21-24C51 9 42 3 26 5" fill="none" stroke="#d9262c" stroke-width="2"/></svg><div class="week-label">WEEK<br>3</div></div><span class="discount">10% OFF</span><span class="item">SKIRTS</span><span class="dates">15/07/24 – 21/07/24</span></li>
        <li class="offer"><div class="week"><svg viewBox="0 0 56 50"><path d="M30 3C12 2 3 14 4 27c1 14 13 21 27 19 15-2 22-11 21-24C51 9 42 3 26 5" fill="none" stroke="#d9262c" stroke-width="2"/></svg><div class="week-label">WEEK<br>4</div></div><span class="discount">10% OFF</span><span class="item">SHIRTS/BLOUSES</span><span class="dates">22/07/24 – 28/07/24</span></li>
        <li class="offer"><div class="week"><svg viewBox="0 0 56 50"><path d="M30 3C12 2 3 14 4 27c1 14 13 21 27 19 15-2 22-11 21-24C51 9 42 3 26 5" fill="none" stroke="#d9262c" stroke-width="2"/></svg><div class="week-label">WEEK<br>5</div></div><span class="discount">10% OFF</span><span class="item">TROUSERS</span><span class="dates">29/07/24 – 04/08/24</span></li>
        <li class="offer"><div class="week"><svg viewBox="0 0 56 50"><path d="M30 3C12 2 3 14 4 27c1 14 13 21 27 19 15-2 22-11 21-24C51 9 42 3 26 5" fill="none" stroke="#d9262c" stroke-width="2"/></svg><div class="week-label">WEEK<br>6</div></div><span class="discount">10% OFF</span><span class="item">SHOES</span><span class="dates">05/08/24 – 11/08/24</span></li>
        <li class="offer"><div class="week"><svg viewBox="0 0 56 50"><path d="M30 3C12 2 3 14 4 27c1 14 13 21 27 19 15-2 22-11 21-24C51 9 42 3 26 5" fill="none" stroke="#d9262c" stroke-width="2"/></svg><div class="week-label">WEEK<br>7</div></div><span class="discount">10% OFF</span><span class="item">BAGS</span><span class="dates">12/08/24 – 18/08/24</span></li>
        <li class="offer"><div class="week"><svg viewBox="0 0 56 50"><path d="M30 3C12 2 3 14 4 27c1 14 13 21 27 19 15-2 22-11 21-24C51 9 42 3 26 5" fill="none" stroke="#d9262c" stroke-width="2"/></svg><div class="week-label">WEEK<br>8</div></div><span class="discount">10% OFF</span><span class="item">HAIR ACCESSORIES</span><span class="dates">19/08/24 – 25/08/24</span></li>
        <li class="offer"><div class="week"><svg viewBox="0 0 56 50"><path d="M30 3C12 2 3 14 4 27c1 14 13 21 27 19 15-2 22-11 21-24C51 9 42 3 26 5" fill="none" stroke="#d9262c" stroke-width="2"/></svg><div class="week-label">WEEK<br>9</div></div><span class="discount">10% OFF</span><span class="item">SHIN PADS/GUM SHIELDS</span><span class="dates">26/08/24 – 01/09/24</span></li>
        <li class="offer"><div class="week"><svg viewBox="0 0 56 50"><path d="M30 3C12 2 3 14 4 27c1 14 13 21 27 19 15-2 22-11 21-24C51 9 42 3 26 5" fill="none" stroke="#d9262c" stroke-width="2"/></svg><div class="week-label">WEEK<br>10</div></div><span class="discount">10% OFF</span><span class="item">NAME TAPES</span><span class="dates">02/09/24 – 08/09/24</span></li>
      </ol>
    </div>

    <p class="tagline">TEN WEEKS OF TEN SPECIAL OFFERS</p>
    <p class="tagline-script">This summer</p>
    <div class="score">
      <svg viewBox="0 0 126 92"><path d="M70 5C32 2 6 22 6 48c0 26 26 40 60 38 34-2 56-20 54-44C118 18 96 4 58 8" fill="none" stroke="#ffffff" stroke-width="3"/></svg>
      <div class="score-text">10/10</div>
    </div>
  </section>
</div>
</body>
</html>
```